Brindle's Business Card

I need some designs for a new business card including the new logo attached. An old example of our business card is also attached to show all the data that should be included on the new design.
**I added some more examples someone had mocked up**

Contact Information for Business Card

Should include all info on other examples uploaded.

```html
<!DOCTYPE html>
<html lang="en">
<head>
<meta charset="utf-8">
<title>Brindle's Business Card</title>
<link rel="stylesheet" href="https://fonts.googleapis.com/css2?family=Montserrat:wght@400;600;700;800&display=swap">
<style>
  :root {
    --bg: #e9eaec;
    --card: #ffffff;
    --blue: #1670b9;
    --red: #e32027;
    --ink: #1c1c1c;
  }
  * { margin: 0; padding: 0; box-sizing: border-box; }
  html, body { width: 1200px; height: 1026px; overflow: hidden; }
  body {
    background: var(--bg);
    font-family: "Montserrat", sans-serif;
    position: relative;
  }
  .card {
    position: absolute;
    left: 290px;
    width: 620px;
    height: 354px;
    background: var(--card);
    box-shadow: 0 6px 18px rgba(0,0,0,0.18);
    overflow: hidden;
  }
  .card-back { top: 110px; }
  .card-front { top: 560px; }
  .back-edge {
    position: absolute; left: 0; right: 0; bottom: 0;
    height: 10px; background: var(--blue);
  }
  .brand {
    position: absolute;
    display: flex; align-items: center; gap: 16px;
  }
  .card-back .brand { left: 118px; top: 118px; }
  .card-front .brand { left: 100px; top: 56px; }
  .brand-dot {
    width: 58px; height: 58px; border-radius: 50%;
    background: var(--red); flex: none;
  }
  .brand-name {
    font-weight: 800; font-size: 62px; line-height: 1;
    color: var(--blue); letter-spacing: 1px;
  }
  .brand-tagline {
    font-weight: 700; font-size: 15.5px; color: var(--red);
    margin-top: 6px; letter-spacing: 0.2px;
  }
  .contact-row {
    position: absolute; left: 70px; top: 204px;
    display: flex; align-items: center;
  }
  .person-name {
    font-weight: 700; font-size: 22px; color: var(--blue);
    padding-right: 22px;
  }
  .divider { width: 2px; height: 34px; background: var(--blue); }
  .contact-list {
    list-style: none; padding-left: 22px;
    font-size: 15px; color: var(--ink);
  }
  .contact-list li { display: flex; align-items: center; gap: 10px; line-height: 22px; }
  .contact-list svg { width: 14px; height: 14px; flex: none; }
  .bands { position: absolute; left: 0; bottom: 0; width: 620px; height: 64px; }
  .band-label {
    position: absolute; font-size: 14px; line-height: 17px; color: #fff;
    letter-spacing: 0.5px; text-transform: uppercase; white-space: nowrap;
  }
  .label-licensed { left: 34px; bottom: 16px; }
  .label-family { right: 24px; bottom: 9px; }
</style>
</head>
<body>
  <section class="card card-back" aria-label="Card back">
    <div class="brand">
      <span class="brand-dot"></span>
      <div>
        <div class="brand-name">BRINDLE'S</div>
        <div class="brand-tagline">AIR CONDITIONING &amp; HEATING SERVICE</div>
      </div>
    </div>
    <div class="back-edge"></div>
  </section>

  <section class="card card-front" aria-label="Card front">
    <div class="brand">
      <span class="brand-dot"></span>
      <div>
        <div class="brand-name">BRINDLE'S</div>
        <div class="brand-tagline">AIR CONDITIONING &amp; HEATING SERVICE</div>
      </div>
    </div>

    <div class="contact-row">
      <div class="person-name">Mark Brindle</div>
      <div class="divider"></div>
      <ul class="contact-list">
        <li>
          <svg viewBox="0 0 16 16"><path fill="#e32027" d="M3 2l3 0 1 4-2 1c1 2 2 3 4 4l1-2 4 1 0 3c0 1-1 2-2 2C6 15 1 10 1 4c0-1 1-2 2-2z"/></svg>
          555.014.2290
        </li>
        <li>
          <svg viewBox="0 0 16 16"><rect x="1" y="3" width="14" height="10" fill="#1670b9"/><path d="M1 3l7 6 7-6" fill="none" stroke="#fff" stroke-width="1.4"/></svg>
          hvacbrindle@mailbox.com
        </li>
      </ul>
    </div>

    <svg class="bands" viewBox="0 0 620 64" preserveAspectRatio="none" aria-hidden="true">
      <polygon points="0,14 340,14 310,64 0,64" fill="#1670b9"/>
      <polygon points="348,30 620,30 620,64 326,64" fill="#e32027"/>
    </svg>
    <span class="band-label label-licensed">Licensed &amp; Insured</span>
    <span class="band-label label-family">Family Owned &amp; Operated</span>
  </section>
</body>
</html>
```